Letterhead Design Project

Professional but modern letterhead.

Target Market(s)

mining companies

Industry/Entity Type

It Professional

Colors

Designer to choose colors to be used in the design.

```html
<!DOCTYPE html>
<html lang="en">
<head>
<meta charset="utf-8">
<title>Kestrel Letterhead</title>
<link rel="stylesheet" href="https://fonts.googleapis.com/css2?family=Arimo:wght@400;700&display=swap">
<style>
  :root {
    --brand-blue: #0d4a91;
    --paper: #ffffff;
    --footer-text: #ffffff;
  }
  * { margin: 0; padding: 0; box-sizing: border-box; }
  html, body { width: 928px; height: 1200px; overflow: hidden; background: var(--paper); }
  body { font-family: "Arimo", Arial, sans-serif; }

  .letterhead { position: relative; width: 928px; height: 1200px; background: var(--paper); }

  .brand { position: absolute; left: 62px; top: 28px; width: 76px; display: flex; flex-direction: column; align-items: center; }
  .brand-dot { width: 58px; height: 58px; border-radius: 50%; background: var(--brand-blue); margin-bottom: 22px; }
  .brand-name { color: var(--brand-blue); font-weight: 700; font-size: 24px; letter-spacing: 0.5px; line-height: 1; white-space: nowrap; }

  .contact-band { position: absolute; left: 0; bottom: 0; width: 928px; height: 72px; background: var(--brand-blue); }
  .band-corner { position: absolute; right: 0; bottom: 0; width: 100px; height: 72px; }
  .corner-dot { position: absolute; right: 22px; bottom: 14px; width: 44px; height: 44px; border-radius: 50%; background: var(--brand-blue); }

  .contact-item { position: absolute; top: 13px; display: flex; align-items: flex-start; color: var(--footer-text); font-size: 11.5px; line-height: 15px; white-space: nowrap; }
  .contact-item svg { flex: none; margin-right: 6px; margin-top: -1px; }
  .contact-address { left: 38px; }
  .contact-phone { left: 190px; }
  .contact-mobile { left: 300px; }
  .contact-fax { left: 406px; }
  .contact-email { left: 521px; }
  .contact-web { left: 707px; }
</style>
</head>
<body>
<div class="letterhead">
  <header class="brand">
    <div class="brand-dot"></div>
    <div class="brand-name">KESTREL</div>
  </header>

  <footer class="contact-band">
    <div class="contact-item contact-address">
      <svg width="12" height="16" viewBox="0 0 12 16"><path d="M6 0a6 6 0 0 0-6 6c0 4.5 6 10 6 10s6-5.5 6-10a6 6 0 0 0-6-6zm0 8.4A2.4 2.4 0 1 1 6 3.6a2.4 2.4 0 0 1 0 4.8z" fill="#fff"/></svg>
      <span>Suite # 410, Birch Bldg,<br>NY 10482</span>
    </div>
    <div class="contact-item contact-phone">
      <svg width="17" height="17" viewBox="0 0 17 17"><circle cx="8.5" cy="8.5" r="7.5" fill="none" stroke="#fff" stroke-width="1.4"/><path d="M5.6 4.6l1.5-.3.9 2-1 .8c.5 1.1 1.3 1.9 2.4 2.4l.8-1 2 .9-.3 1.5c-3.4.2-6.5-2.9-6.3-6.3z" fill="#fff"/></svg>
      <span>555-204-7731</span>
    </div>
    <div class="contact-item contact-mobile">
      <svg width="10" height="16" viewBox="0 0 10 16"><rect x="0.5" y="0.5" width="9" height="15" rx="1.5" fill="#fff"/><rect x="2" y="2.5" width="6" height="8" fill="#0d4a91"/><circle cx="5" cy="13" r="1" fill="#0d4a91"/></svg>
      <span>555-318-6420</span>
    </div>
    <div class="contact-item contact-fax">
      <span>Fax : 555-762-0953</span>
    </div>
    <div class="contact-item contact-email">
      <svg width="16" height="12" viewBox="0 0 16 12"><path d="M0 4l8-4 8 4v8H0z" fill="#fff"/><path d="M1.5 4.6L8 8.4l6.5-3.8" fill="none" stroke="#0d4a91" stroke-width="1.1"/></svg>
      <span>hello@kestreldata.com</span>
    </div>
    <div class="contact-item contact-web">
      <span>www.kestreldata.com</span>
    </div>
    <svg class="band-corner" viewBox="0 0 100 72" preserveAspectRatio="none"><polygon points="32,0 100,0 100,72 0,72" fill="#fff"/></svg>
    <div class="corner-dot"></div>
  </footer>
</div>
</body>
</html>
```